Human Resources consulting firm website

I recently started a consulting firm after 30 years in Human Resources (Executive Development) work with Kestrel 25 companies. I am looking for a website design that will convey both the services I provide (all in the HR / executive development arena) as well as sense of trust in me and my abilities (many years of experience, breadth of knowledge).

In the attachment section, there is a document with links to a number of websites fr firms that do similar work to me - the doc shares what I like about them and what I do not. I've also include my bio to give you a sens of who I am /what I do. The head shot will be replaced soon as I'm having new photos take, but the verbiage is what's important.

I need your help with the look and feel as well as different ideas on how to share the info. I am looking for your creativity and experience. I have not done a website for anything in the past.

Looking forward to working together on a great project and product!!

Target Market(s)

Any company looking for senior leader caoching, assessments of those leaders or help with a CEO transition. My wheelhouse is Kestrel top 100 companies, but am able to work with small firms as well. Also any Board of Directors and upstarts in California.

Industry/Entity Type

Consulting

Coding

Coded - Design and coding required

Number of Pages Required

5+ page

Font styles to use
Sans Serif
Other font styles liked:
• Do not have a specific one but am very open to options

Colors

Designer to choose colors to be used in the design.

Requirements
Must have
• My project must have be professional (see the type of companies I am targeting) with an air of simplicity.
• A professional yet approachable look and feel that delivers:
• (1) I want there to be a landing page (with limited info - a more of a "teaser")
• (2) a tab for about us (with a few sentences about the company, my photo and option to link to my bio)
• (3) a tab for the services offered (one page with tiles that have a little bit about the services and the option to link to more info)
• (4) a tab to contact me (form to fill out with some personal info and the request that will get sent to my email).
• (5) diversity in the imagery
• (6) I plan for it to be mostly static. I will not be adding/changing regularly (although imagine the first couple months will want to tweak it as I get feedback). I do not plan to add blogs, etc.
Nice to have
• (1) Good graphics. I'm ok with black and white if it's classic or color photos. I don't want stalk photos anyone can get on the web. A sophisticated yet approachable look is what I'm going for.
• (2) Ability to get to know me (the principal) just a bit. That can be through the verbiage, colors, photos, etc.
• (3) Ability to contact me from the front home/landing page or contact page.
• (4) When someone looks me up on line, I want them to see a sentence or two about the company and have links that will take them straight to the page on the website they are looking for (contact, about us, etc.)
Should not have
• I do not want this to be:
• (1) overly feminine (not pink, purple, etc.),
• (2) flashy (I'm fine with a small video or moving photo but doubt I want anything beyond that) or
• (3) too close to the "out there" category (this is a professional business with corporate clients).
• (4) sterile (I'm selling myself .. that's what people buy when they hire a consultant).
• (5) basic - I do not want this to look like I hired my nephew straight out of college to build this. I'm looking for a strong, professional look.

```html
<!DOCTYPE html>
<html lang="en">
<head>
<meta charset="utf-8">
<title>About – Whitfield Talent Solutions</title>
<link href="https://fonts.googleapis.com/css2?family=Jost:ital,wght@0,400;0,500;0,600;1,600&family=Crimson+Pro:wght@400&display=swap" rel="stylesheet">
<style>
:root{
  --stage:#0f4277;
  --navy:#0d3e70;
  --sky:#8ab8e3;
  --sky-deep:#6f9fd2;
  --ink:#1c1c1c;
  --paper:#ffffff;
  --mist:#f5f5f5;
  --footer:#333333;
  --sans:'Jost',Arial,sans-serif;
  --serif:'Crimson Pro',Georgia,serif;
}
*{box-sizing:border-box;margin:0;padding:0}
html,body{width:1200px;height:3344px;overflow:hidden;background:var(--stage);font-family:var(--sans);color:var(--ink)}
.page{position:absolute;left:215px;top:228px;width:770px;height:2909px;background:var(--paper)}
.wordmark{display:flex;align-items:center;gap:7px;color:var(--sky-deep);font:500 9px/10px var(--sans);letter-spacing:.4px;text-transform:uppercase}
.wordmark .dot{width:10px;height:10px;background:currentColor}
.nav{position:absolute;left:0;top:0;width:770px;height:58px;background:var(--paper)}
.nav .wordmark{position:absolute;left:30px;top:14px}
.nav-link{position:absolute;top:25px;font:600 8px var(--sans);letter-spacing:.6px;color:var(--ink)}
.nav-link.active{color:var(--navy);border-bottom:2px solid var(--navy);padding-bottom:3px}
.nav-icon{position:absolute;top:25px;width:9px;height:9px;background:var(--ink)}
.hero{position:absolute;top:58px;left:0;width:770px;height:239px;background:var(--sky)}
.hero h1{position:absolute;left:51px;top:62px;font:400 34px var(--serif);color:var(--navy)}
.hero p{position:absolute;left:51px;top:122px;width:470px;font:400 17px/30px var(--sans);color:#fff}
.story{position:absolute;top:297px;left:0;width:770px;height:376px;background:var(--paper)}
.label{font:600 8.5px var(--sans);letter-spacing:1.2px;color:var(--navy);text-transform:uppercase}
.story .label{position:absolute;left:51px;top:66px}
.story .copy{position:absolute;left:51px;top:87px;width:284px;font:400 11.2px/19px var(--sans)}
.btn{position:absolute;left:51px;top:278px;width:143px;height:31px;border:2px solid var(--navy);color:var(--navy);font:600 8.5px/27px var(--sans);letter-spacing:1px;text-align:center}
.photo{position:absolute}
.story .photo{left:374px;top:40px;width:396px;height:296px;background:
  radial-gradient(ellipse 22% 30% at 55% 38%,rgba(214,160,120,.75),transparent 70%),
  radial-gradient(ellipse 30% 40% at 22% 30%,rgba(120,84,60,.7),transparent 70%),
  radial-gradient(ellipse 40% 30% at 60% 70%,rgba(32,88,170,.9),transparent 75%),
  radial-gradient(ellipse 25% 30% at 86% 70%,rgba(190,225,230,.8),transparent 70%),
  linear-gradient(180deg,#141c2a 0%,#1f2f48 50%,#5d7b9c 85%,#c9d4de 100%)}
.tagline{position:absolute;top:673px;left:0;width:770px;height:239px;background:
  radial-gradient(ellipse 50% 25% at 35% 40%,rgba(105,150,205,.55),transparent 75%),
  linear-gradient(180deg,#a3c7ec 0%,#8ab8e3 35%,#7aa8da 60%,#8ab8e3 100%)}
.tagline p{position:absolute;left:0;width:770px;top:100px;text-align:center;font:400 27px var(--serif);color:#fff}
.founder{position:absolute;top:912px;left:0;width:770px;height:1804px;background:var(--mist)}
.card{position:absolute;left:35px;top:55px;width:702px;height:1560px;background:var(--paper)}
.card .portrait{left:60px;top:45px;width:247px;height:372px;background:
  radial-gradient(ellipse 45% 55% at 50% 88%,rgba(28,24,26,.95),transparent 72%),
  radial-gradient(ellipse 40% 42% at 50% 40%,rgba(110,62,38,.85),transparent 72%),
  radial-gradient(ellipse 24% 24% at 50% 40%,rgba(228,176,150,.9),transparent 75%),
  radial-gradient(ellipse at 50% 35%,#cfe5f8 0%,#7eb4e6 55%,#3d7fc4 100%)}
.card > .label{position:absolute;left:359px;top:66px}
.lead{font:400 19px/21px var(--serif);color:var(--navy)}
.card .lead.side{position:absolute;left:359px;top:92px;width:290px}
.body{font:400 11.2px/19px var(--sans)}
.card .body.side{position:absolute;left:359px;top:170px;width:282px}
.card .lead.center{position:absolute;left:0;width:702px;top:477px;text-align:center}
.card .body.wide{position:absolute;left:136px;width:444px}
.card .team{left:60px;top:874px;width:580px;height:257px;background:
  radial-gradient(ellipse 18% 35% at 22% 55%,rgba(110,86,70,.85),transparent 72%),
  radial-gradient(ellipse 20% 40% at 83% 62%,rgba(70,110,160,.9),transparent 72%),
  radial-gradient(ellipse 22% 25% at 50% 72%,rgba(70,120,60,.75),transparent 72%),
  linear-gradient(180deg,transparent 70%,rgba(90,80,70,.55) 100%),
  linear-gradient(90deg,#d8d4cc 0%,#e6d38a 40%,#ecd680 62%,#c9b978 100%)}
.team-note{position:absolute;right:16px;top:38px;font:italic 600 9.5px var(--sans);color:#fff}
.cta{position:absolute;left:32px;top:2618px;width:707px;height:117px;background:var(--navy);z-index:2}
.cta .label{position:absolute;left:32px;top:33px;color:#fff}
.cta p{position:absolute;left:32px;top:54px;font:400 16px var(--sans);color:#fff}
.cta .ghost{position:absolute;left:512px;top:38px;width:157px;height:44px;border:2px solid #fff;color:#fff;font:600 9px/40px var(--sans);letter-spacing:1px;text-align:center}
.footer{position:absolute;top:2716px;left:0;width:770px;height:193px;background:var(--footer)}
.footer .wordmark{position:absolute;left:45px;top:80px;color:#fff}
.fcol{position:absolute;top:78px;font:400 9px/17.5px var(--sans);color:#e6e6e6;list-style:none}
.fcol .sq{display:inline-block;width:7px;height:7px;background:#e6e6e6;margin-right:4px}
</style>
</head>
<body>
<div class="page">
  <header class="nav">
    <div class="wordmark"><span class="dot"></span><span>Whitfield<br>Talent<br>Solutions</span></div>
    <span class="nav-link active" style="left:511px">ABOUT</span>
    <span class="nav-link" style="left:566px">SERVICES</span>
    <span class="nav-link" style="left:629px">CONTACT</span>
    <span class="nav-icon" style="left:710px"></span>
    <span class="nav-icon" style="left:731px;width:6px"></span>
  </header>

  <section class="hero">
    <h1>About Us</h1>
    <p>Short description about what Whitfield Talent Solution does. Lorem ipsum dolor sit amet, consectetur adipiscing elit.</p>
  </section>

  <section class="story">
    <div class="label">Our Story</div>
    <p class="copy">Short paragraph of Whitfield Talent Solution. Lorem ipsum dolor sit amet, consectetur adipiscing elit, sed do eiusmod tempor incididunt ut labore et dolore magna aliqua. Ut enim ad minim veniam, quis nostrud exercitation ullamco laboris nisi. Duis aute irure dolor in reprehenderit in voluptate velit esse cillum dolore, quis nostrud exercitation ullamco laboris nisi.</p>
    <div class="btn">MEET THE FOUNDER ↓</div>
    <div class="photo" role="img" aria-label="Photo of a diverse team smiling at their desks in a modern office"></div>
  </section>

  <section class="tagline" role="img" aria-label="Faded blue city skyline behind the tagline">
    <p>Tagline or Quote can go here</p>
  </section>

  <section class="founder">
    <article class="card">
      <div class="photo portrait" role="img" aria-label="Portrait of the founder, Claire Whitfield, against a blue backdrop"></div>
      <div class="label">About the Founder</div>
      <p class="lead side">Claire Whitfield is a highly respected, sought-after talent management expert focused on the full talent ecosystem.</p>
      <p class="body side">Her depth of expertise includes talent management, assessment, succession planning, organizational development, as well as identifying and developing critical talent. She quickly and effectively connects talent strategies to business strategies, coaching and advising leaders to increase their effectiveness while staying aligned to company goals. Claire has worked extensively with global professionals with an emphasis on executives including CEOs and Boards of Directors. She is routinely asked to coach and counsel senior leaders to improve their performance and therefore the organizations’ success.</p>
      <p class="lead center">Claire is the principal and founder of Whitfield Talent Solutions,<br>a talent leadership firm with 30 years of global experience<br>developing and impacting talent agendas.</p>
      <p class="body wide" style="top:608px">Claire is the principal and founder of Whitfield Talent Solutions, a talent leadership firm with 30 years of global experience developing and impacting talent agendas. Most of her career has been spent working with and for Kestrel top 50 companies. Her corporate path includes 25+ years at Meridian Industrial driving talent management strategy: managing the development of top leaders, leading the organization and talent matrix across 170+ countries, and curating the Board of Directors’ knowledge of the talent. Claire’s depth of experience regarding what a Board of Directors wants – and needs – from a talent perspective is one of the capabilities that sets her apart. She has spent more than a decade developing and executing CEO and direct report succession plans as well as creating and implementing opportunities for Boards to deepen their knowledge of critical talent.</p>
      <div class="photo team" role="img" aria-label="Photo of colleagues collaborating across a table in a bright office">
        <span class="team-note">(temporary image)</span>
      </div>
      <p class="body wide" style="top:1200px">Claire’s background and education are based in finance and business administration. She is data driven with an innovative mindset continuously looking for new ways to do things and piloting transformations in and around talent management. She pushes the boundaries of both people and processes to see what is possible. Examples of such success include: C-suite coaching producing better leaders performing at a higher level, wing-to-wing talent processes at scale that result in effective and actionable outcomes, upskilling people leaders to elevate their (and their teams’) performance, creative executive assessment processes providing data for both the assessed and the company to act on. Claire is considered a trusted, strategic advisor with a bias for inclusion. Her depth of talent and leadership knowledge allows her to step back and apply a critical eye to potential talent decisions ensuring alignment with overall business imperatives.</p>
      <p class="body wide" style="top:1450px">Claire holds a bachelor’s degree in Finance and Financial Management Services from Lakeshore State University. She lives in southern California with her husband Tom. They have two grown sons.</p>
    </article>
  </section>

  <aside class="cta">
    <div class="label">Contact Us</div>
    <p>We would love to collaborate with you</p>
    <div class="ghost">GET IN TOUCH</div>
  </aside>

  <footer class="footer">
    <div class="wordmark"><span class="dot"></span><span>Whitfield<br>Talent<br>Solutions</span></div>
    <ul class="fcol" style="left:378px"><li>Home</li><li>About</li><li>Services</li><li>Contact</li></ul>
    <ul class="fcol" style="left:465px"><li><span class="sq"></span>Network</li><li><span class="sq"></span>Social</li></ul>
    <ul class="fcol" style="left:572px"><li>WHITFIELD TALENT SOLUTIONS</li><li>hello@whitfield-talent.example</li><li>123.456.7890</li></ul>
  </footer>
</div>
</body>
</html>
```